Business Card for a mobile physiotherapy company

I need a layout for a business card for a mobile physiotherapy company.
Slogan is "Mobile Physiotherapy - Your Road To Recovery"
Phone number is 867-402-5913
Email VantrePhysio@mailbright.ca (subject to change with website)
Website www.VantrePhysio.ca
My name and credentials: Kent Vantre Kent Vantre, BSc(kin), MPT, CAFCI, IMS
Information maybe included: Direct Billing, Services including Physiotherapy, IMS, acupuncture
Maybe include facebook and instagram logos
One side with the logo clean and sharp
Other side with details, try not to look too busy, keep everything concise

```html
<!DOCTYPE html>
<html lang="en">
<head>
<meta charset="utf-8">
<title>Vantre Therapy – Business Card</title>
<link href="https://fonts.googleapis.com/css2?family=Lato:wght@400;700&display=swap" rel="stylesheet">
<style>
  :root {
    --backdrop: #3b3b3b;
    --teal: #11574b;
    --teal-dark: #0d4a40;
    --navy: #2d4b7e;
    --white: #ffffff;
    --ink-teal: #1d6a5c;
  }
  * { box-sizing: border-box; margin: 0; padding: 0; }
  html, body {
    width: 1200px;
    height: 900px;
    overflow: hidden;
    background: var(--backdrop);
    font-family: "Lato", sans-serif;
  }
  .sheet {
    width: 1200px;
    height: 900px;
    display: flex;
    flex-direction: column;
    align-items: center;
    justify-content: center;
    gap: 50px;
  }
  .card {
    position: relative;
    width: 700px;
    height: 400px;
    overflow: hidden;
    box-shadow: 0 10px 30px rgba(0,0,0,.35);
  }

  /* Front: logo side */
  .card--front {
    background: radial-gradient(circle at 60% 40%, var(--teal) 0%, var(--teal-dark) 100%);
    color: var(--white);
    display: flex;
    flex-direction: column;
    align-items: center;
    justify-content: center;
  }
  .brand {
    display: flex;
    align-items: center;
    gap: 14px;
    font-weight: 700;
    font-size: 44px;
    letter-spacing: 6px;
    color: var(--white);
  }
  .brand__mark {
    width: 18px;
    height: 18px;
    background: var(--white);
  }
  .slogan {
    margin-top: 26px;
    font-size: 20px;
    letter-spacing: .3px;
  }

  /* Back: details side */
  .card--back { background: var(--white); }
  .card__band {
    position: absolute;
    inset: 0;
    width: 700px;
    height: 400px;
  }
  .holder {
    position: absolute;
    top: 38px;
    right: 36px;
    text-align: right;
  }
  .holder__name {
    font-size: 31px;
    color: var(--navy);
    font-weight: 400;
  }
  .holder__services {
    margin-top: 6px;
    font-size: 15px;
    color: var(--ink-teal);
  }
  .band-brand {
    position: absolute;
    top: 196px;
    left: 250px;
    display: flex;
    align-items: center;
    gap: 10px;
    font-size: 26px;
    font-weight: 700;
    letter-spacing: 4px;
    color: var(--white);
  }
  .band-brand__mark {
    width: 12px;
    height: 12px;
    background: var(--white);
  }
  .contact {
    position: absolute;
    left: 36px;
    bottom: 36px;
    font-size: 17px;
    color: var(--ink-teal);
  }
  .contact__sep { margin: 0 6px; }
</style>
</head>
<body>
  <main class="sheet">
    <section class="card card--front" aria-label="Card front">
      <div class="brand">
        <span class="brand__mark" aria-hidden="true"></span>
        <span class="brand__name">VANTRE THERAPY</span>
      </div>
      <p class="slogan">Mobile Physiotherapy - Your Road To Recovery</p>
    </section>

    <section class="card card--back" aria-label="Card back">
      <svg class="card__band" viewBox="0 0 700 400" aria-hidden="true">
        <polygon points="60,300 230,128 700,128 700,300" fill="var(--teal)"/>
      </svg>
      <div class="holder">
        <h1 class="holder__name">Kent Vantre, BSc(kin),MPT, CAFCI, IMS</h1>
        <p class="holder__services">Direct Billing Services including Physiotherapy, IMS, acupuncture</p>
      </div>
      <div class="band-brand">
        <span class="band-brand__mark" aria-hidden="true"></span>
        <span>VANTRE THERAPY</span>
      </div>
      <p class="contact">
        P: 867-402-5913<span class="contact__sep">|</span>E: VantrePhysio@mailbright.ca<span class="contact__sep">|</span>W: www.VantrePhysio.ca
      </p>
    </section>
  </main>
</body>
</html>
```